Rebrand of an existing product label

We are looking for a new design / label for our body lotion. Attached is the current product label. We have this product available in Retinol, Collagen, Hyaluronic Acid, Vitamin C, and Coconut. The brand should reflect a clinical, trustworthy look. We also want to include on the label that the product contains Dead Sea Minerals. Attached is the dieline for the label for the jar and the top. This jar is the packaging that needs to be used for this project.
Updates

Target Market(s)

40+

Requirements
Must have
• Ingredient callouts on the front + benefits. Ex- Vitamin C Brightening Cream

```html
<!DOCTYPE html>
<html lang="en">
<head>
<meta charset="UTF-8">
<title>Dermavale Collagen Firming Cream Label</title>
<link href="https://fonts.googleapis.com/css2?family=Cinzel:wght@900&family=Josefin+Sans:wght@400&family=Montserrat:wght@300;400;600;700&display=swap" rel="stylesheet">
<style>
  :root {
    --band-blue: #8dd7f3;
    --accent-blue: #7ccdee;
    --rule-blue: #a9def4;
    --ink: #0b0b0b;
    --paper: #ffffff;
    --label-white: #f6f7f8;
  }
  * { margin: 0; padding: 0; box-sizing: border-box; }
  html, body {
    width: 1200px;
    height: 673px;
    overflow: hidden;
    background: var(--paper);
  }
  .label {
    position: relative;
    width: 1200px;
    height: 673px;
    background: var(--label-white);
    font-family: "Montserrat", sans-serif;
  }
  .label__band {
    position: absolute;
    left: 0; top: 0;
    width: 100%;
    height: 458px;
    background: var(--band-blue);
  }
  .label__scallop {
    position: absolute;
    left: 0; top: 450px;
    width: 100%;
    height: 16px;
    background: radial-gradient(circle at 8px 8px, var(--label-white) 6px, transparent 6.5px) 0 0 / 16px 16px repeat-x;
  }
  .mineral-badge {
    position: absolute;
    left: 40px; top: 62px;
    width: 140px; height: 140px;
    border: 2px solid var(--paper);
    border-radius: 50%;
    display: flex;
    flex-direction: column;
    align-items: center;
    justify-content: center;
    text-align: center;
    color: var(--paper);
    font-weight: 700;
    font-size: 14px;
    line-height: 1.25;
    letter-spacing: 0.5px;
  }
  .mineral-badge__lead { font-weight: 400; font-size: 12px; }
  .brand {
    position: absolute;
    left: 0; top: 88px;
    width: 100%;
    display: flex;
    justify-content: center;
    align-items: center;
    gap: 18px;
  }
  .brand__dot {
    width: 22px; height: 22px;
    border-radius: 50%;
    background: var(--ink);
  }
  .brand__name {
    font-family: "Josefin Sans", sans-serif;
    font-weight: 400;
    font-size: 76px;
    line-height: 1;
    color: var(--ink);
    letter-spacing: 1px;
    padding-top: 10px;
  }
  .size-tag {
    position: absolute;
    left: 0; top: 208px;
    width: 100%;
    text-align: center;
    font-weight: 600;
    font-size: 26px;
    color: var(--paper);
    letter-spacing: 0.5px;
  }
  .product-name {
    position: absolute;
    left: 0; top: 256px;
    width: 100%;
    text-align: center;
    font-family: "Cinzel", serif;
    font-weight: 900;
    font-size: 140px;
    line-height: 1;
    color: var(--ink);
    letter-spacing: 4px;
  }
  .product-type {
    position: absolute;
    left: 0; top: 406px;
    width: 100%;
    text-align: center;
    font-weight: 600;
    font-size: 24px;
    line-height: 1;
    color: var(--paper);
    letter-spacing: 6px;
  }
  .info-table {
    position: absolute;
    left: 145px; top: 494px;
    width: 906px; height: 162px;
    border: 2px solid var(--rule-blue);
    display: grid;
    grid-template-columns: 547px 1fr;
    grid-template-rows: 96px 1fr;
  }
  .info-table__cell {
    border-right: 2px solid var(--rule-blue);
    border-bottom: 2px solid var(--rule-blue);
    display: flex;
    align-items: center;
    padding: 0 14px;
  }
  .info-table__cell:nth-child(2n) { border-right: none; }
  .info-table__cell:nth-child(n+3) { border-bottom: none; }
  .benefit {
    font-weight: 700;
    font-size: 25px;
    line-height: 1;
    color: var(--accent-blue);
    text-transform: uppercase;
  }
  .benefit__lead { font-weight: 400; }
  .usage {
    font-weight: 700;
    font-size: 24px;
    color: var(--ink);
  }
  .texture-swatch {
    width: 100%; height: 80px;
    background: linear-gradient(90deg, var(--accent-blue), var(--band-blue), var(--accent-blue));
  }
  .info-table__cell--volume { justify-content: center; }
  .volume {
    font-weight: 700;
    font-size: 24px;
    color: var(--ink);
  }
  .volume__metric { font-weight: 300; }
</style>
</head>
<body>
  <div class="label">
    <div class="label__band"></div>
    <div class="label__scallop"></div>

    <div class="mineral-badge">
      <span class="mineral-badge__lead">WITH</span>
      <span>DEAD SEA</span>
      <span>MINERALS</span>
    </div>

    <div class="brand">
      <span class="brand__dot"></span>
      <span class="brand__name">DERMAVALE</span>
    </div>

    <p class="size-tag">PROFESSIONAL SIZE</p>
    <h1 class="product-name">COLLAGEN</h1>
    <p class="product-type">FIRMING CREAM</p>

    <div class="info-table">
      <div class="info-table__cell">
        <p class="benefit"><span class="benefit__lead">For</span> Radiant, Soft &amp;<br>Healthier Looking Skin</p>
      </div>
      <div class="info-table__cell">
        <div class="texture-swatch" role="img" aria-label="Decorative blue leaf-vein pattern"></div>
      </div>
      <div class="info-table__cell">
        <p class="usage">FOR FACE, NECK &amp; HANDS</p>
      </div>
      <div class="info-table__cell info-table__cell--volume">
        <p class="volume">16.9 FL OZ <span class="volume__metric">(500 ML)</span></p>
      </div>
    </div>
  </div>
</body>
</html>
```